Business Card Design (NEW FILES)

ATTENTION: New vector files are available. Please update your design to reflect/use the new (better resolution) logo images.

Seeking a unique and professional business card design for a commercial drone photography/videography business. The layout should feature
the logo (attached) and include the following information:
978-512-6037
www.skyvantmedia.com
ORD Certified Remote Pilot

```html
<!DOCTYPE html>
<html lang="en">
<head>
<meta charset="utf-8">
<title>Skyvant Media – Business Card</title>
<link rel="stylesheet" href="https://fonts.googleapis.com/css2?family=Montserrat:wght@400;600;700&display=swap">
<style>
  :root {
    --navy: #161b4d;
    --orange: #ee8a4e;
    --white: #ffffff;
    --stage: #e9e9ec;
    --card-shadow: rgba(0, 0, 0, 0.18);
  }
  * { box-sizing: border-box; margin: 0; padding: 0; }
  html, body {
    width: 1200px;
    height: 900px;
    overflow: hidden;
    background: var(--stage);
    font-family: "Montserrat", Arial, sans-serif;
  }
  .stage {
    position: relative;
    width: 1200px;
    height: 900px;
  }
  .card {
    position: absolute;
    top: 301px;
    width: 514px;
    height: 297px;
    background: var(--white);
    box-shadow: 0 4px 14px var(--card-shadow);
    overflow: hidden;
  }
  .card--front { left: 72px; }
  .card--back { left: 616px; }

  /* Front */
  .brand {
    position: absolute;
    left: 0;
    right: 0;
    top: 0;
    bottom: 0;
    display: flex;
    align-items: center;
    justify-content: center;
  }
  .brand-name {
    display: inline-flex;
    align-items: center;
    gap: 12px;
    color: var(--navy);
    font-weight: 600;
    font-size: 34px;
    letter-spacing: 1px;
  }
  .brand-dot {
    width: 18px;
    height: 18px;
    border-radius: 50%;
    background: var(--orange);
  }

  /* Back */
  .credentials {
    position: absolute;
    left: 28px;
    top: 28px;
    color: var(--orange);
    font-weight: 700;
    font-size: 13px;
    line-height: 18px;
    letter-spacing: 0.3px;
  }
  .holder {
    position: absolute;
    left: 28px;
    top: 147px;
  }
  .holder-name {
    color: var(--navy);
    font-weight: 700;
    font-size: 27px;
    line-height: 32px;
    letter-spacing: 0.6px;
  }
  .holder-role {
    margin-top: 2px;
    color: var(--orange);
    font-weight: 700;
    font-size: 15px;
    letter-spacing: 0.4px;
  }
  .contact-band {
    position: absolute;
    left: 0;
    right: 0;
    bottom: 0;
    height: 90px;
    background: var(--navy);
  }
  .contact {
    position: absolute;
    left: 28px;
    top: 16px;
    color: var(--white);
    font-weight: 700;
    font-size: 22px;
    line-height: 29px;
    letter-spacing: 0.4px;
  }
  .hero-art {
    position: absolute;
    right: 0;
    top: 36px;
    width: 112px;
    height: 261px;
    background: linear-gradient(160deg, #2a3170 0%, var(--navy) 55%, #3a3f7a 100%);
  }
</style>
</head>
<body>
  <main class="stage">
    <section class="card card--front" aria-label="Business card front">
      <div class="brand">
        <div class="brand-name"><span>SKYVANT MEDIA</span><span class="brand-dot"></span></div>
      </div>
    </section>

    <section class="card card--back" aria-label="Business card back">
      <p class="credentials">ORD CERTIFIED REMOTE PILOT<br>FULLY INSURED</p>
      <div class="holder">
        <p class="holder-name">MARK DOYLE</p>
        <p class="holder-role">OWNER</p>
      </div>
      <div class="contact-band">
        <p class="contact">978-512-6037<br>WWW.SKYVANTMEDIA.COM</p>
      </div>
      <div class="hero-art" role="img" aria-label="Large drone with camera illustration in navy"></div>
    </section>
  </main>
</body>
</html>
```